LUMIVO Business Card

provide hypnotherapy and counselling for addictions, weight loss, anxiety, depression, smoking, alcohol etc
i would like the design to fit in with a feeling of peace and tranquility

Industry/Entity Type

Hypnotherapy

Contact Information for Business Card

Janet Callory
Clinical Hypnotherapist and Counsellor
BA Social Work
Dip Clinical Hypnotherapy and Psychotherapy

Phone: 0438157302
Email: astillbrookhypnotherapy@fernmail.example

```html
<!DOCTYPE html>
<html lang="en">
<head>
<meta charset="utf-8">
<title>LUMIVO Business Card</title>
<link rel="stylesheet" href="https://fonts.googleapis.com/css2?family=Arimo:wght@400;700&display=swap">
<style>
  :root {
    --page-bg: #dfe9f2;
    --card-bg: #ffffff;
    --name-ink: #4a3b39;
    --body-ink: #3b3131;
    --contact-ink: #111111;
    --qual-blue: #8dbbe3;
    --brand-blue: #3aaee6;
    --band-blue: #8fb5d6;
    --band-sand: #e6e5da;
  }
  * { margin: 0; padding: 0; box-sizing: border-box; }
  html, body {
    width: 1200px;
    height: 1200px;
    overflow: hidden;
    background: var(--page-bg);
    font-family: "Arimo", Arial, sans-serif;
  }
  .card {
    position: absolute;
    left: 50px;
    top: 284px;
    width: 1100px;
    height: 632px;
    background: var(--card-bg);
    overflow: hidden;
    box-shadow: 0 2px 10px rgba(40, 80, 120, 0.15);
  }
  .card__band {
    position: absolute;
    left: 0;
    bottom: 0;
    width: 100%;
    height: 140px;
    background:
      linear-gradient(180deg, var(--card-bg) 0%, rgba(255, 255, 255, 0) 55%),
      linear-gradient(90deg, var(--band-sand) 0%, var(--band-blue) 30%, var(--band-sand) 62%, var(--band-blue) 100%);
  }
  .brand {
    position: absolute;
    left: 179px;
    top: 158px;
    display: flex;
    align-items: center;
    gap: 20px;
  }
  .brand__dot {
    width: 70px;
    height: 70px;
    border-radius: 50%;
    background: var(--brand-blue);
  }
  .brand__name {
    font-weight: 700;
    font-size: 48px;
    letter-spacing: 2px;
    color: var(--brand-blue);
  }
  .identity {
    position: absolute;
    right: 145px;
    top: 312px;
    text-align: right;
  }
  .identity__name {
    font-weight: 700;
    font-size: 51px;
    line-height: 1;
    color: var(--name-ink);
  }
  .identity__role {
    font-size: 29px;
    line-height: 1.1;
    color: var(--body-ink);
  }
  .qualifications {
    position: absolute;
    left: 196px;
    top: 366px;
    font-size: 27px;
    line-height: 36px;
    color: var(--qual-blue);
  }
  .contact {
    position: absolute;
    bottom: 14px;
    font-size: 28px;
    color: var(--contact-ink);
  }
  .contact--phone { left: 18px; }
  .contact--email { right: 26px; }
</style>
</head>
<body>
  <main class="card">
    <div class="card__band" role="img" aria-label="Soft layered waves in calm blue and sand tones along the card's lower edge"></div>

    <div class="brand">
      <span class="brand__dot"></span>
      <span class="brand__name">LUMIVO</span>
    </div>

    <div class="identity">
      <h1 class="identity__name">Janet Callory</h1>
      <p class="identity__role">Clinical Hypnotherapist and Counsellor</p>
    </div>

    <div class="qualifications">
      <p>BA Social Work</p>
      <p>Dip Clinical Hypnotherapy and Psychotherapy</p>
    </div>

    <p class="contact contact--phone">ph/ 0438157302</p>
    <p class="contact contact--email">astillbrookhypnotherapy@fernmail.example</p>
  </main>
</body>
</html>
```